Clean business card with logo provided

I want a card that will stand out among the masses. I need the color and image to show professionalism and yet have a family appeal showing that I only deal with win/win scenarios. The back of the card will be used to take notes about the individual so I can use that in my database entry. I like modern design but need professionalism in it also. It needs to fit my "clean, safe, and affordable housing" motto. I need to be able to write on the file and update the card details for my employees.

Target Market(s)

Investors looking to make investment income through real estate

Industry/Entity Type

Real Estate

Contact Information for Business Card

Mark Dunthorpe
blank address, city, st, zip code
480-555-3174
markdunthorpe@brivoholdings.example
www.brivoholdings.example

Font styles to use
Sans Serif

Requirements
Must have
• I would like the back of the card to have lines for info. example
• Met/Visited: Date:
• Interets:
Nice to have
• I want the cards color to match the logo background color. Font with details to be san serif and black. I want the card rectangular with square corners. Standard business card size. I would like to see cards designed with both images to see which i prefer more.

```html
<!DOCTYPE html>
<html lang="en">
<head>
<meta charset="utf-8">
<title>Brivo Holdings LLC – Business Card</title>
<link rel="stylesheet" href="https://fonts.googleapis.com/css2?family=Open+Sans:wght@400;600;700&display=swap">
<style>
  :root {
    --teal: #00b6cd;
    --teal-deep: #009fb4;
    --ink: #111418;
    --paper: #ffffff;
    --stage: #eef1f3;
    --rule: #1b1f24;
  }
  * { box-sizing: border-box; margin: 0; padding: 0; }
  html, body { width: 1200px; height: 900px; overflow: hidden; }
  body {
    background: var(--stage);
    font-family: "Open Sans", sans-serif;
    position: relative;
  }
  .card {
    position: absolute;
    width: 540px;
    height: 308px;
    overflow: hidden;
    box-shadow: 0 6px 18px rgba(0,0,0,0.12);
  }

  /* Back: note-taking side */
  .card-back { left: 90px; top: 100px; background: var(--paper); }
  .card-back .top-band {
    position: absolute; left: 0; top: 0; width: 100%; height: 64px;
    background: var(--teal);
  }
  .card-back .band-rule {
    position: absolute; left: 0; top: 72px; width: 100%; height: 3px;
    background: var(--teal);
  }
  .note-fields {
    position: absolute; left: 0; top: 118px; width: 100%;
    list-style: none;
  }
  .note-field {
    display: flex; align-items: flex-end;
    height: 56px;
  }
  .note-label {
    width: 200px; text-align: right; padding-right: 14px;
    color: var(--teal); font-weight: 600; font-size: 17px; letter-spacing: 0.5px;
    line-height: 1;
  }
  .note-line { flex: 0 0 280px; height: 12px; }

  /* Front: contact side */
  .card-front { left: 570px; top: 480px; background: var(--teal); color: var(--ink); }
  .brand {
    position: absolute; left: 28px; top: 62px; width: 300px;
    color: var(--paper);
  }
  .brand-name {
    display: flex; align-items: center; gap: 8px;
    font-weight: 600; font-size: 21px; letter-spacing: 1px; line-height: 1;
    white-space: nowrap;
  }
  .brand-dot { width: 12px; height: 12px; border-radius: 50%; background: var(--paper); flex: none; }
  .brand-tagline {
    margin-top: 8px; font-size: 10.5px; letter-spacing: 0.3px;
  }
  .contact {
    position: absolute; left: 268px; top: 112px; width: 256px;
    font-size: 12.5px; line-height: 1.25;
  }
  .contact-name { font-weight: 700; font-size: 16px; margin-bottom: 12px; }
  .contact-address { margin-bottom: 12px; }
  .contact-list { list-style: none; }
  .contact-list li { display: flex; align-items: center; gap: 8px; margin-bottom: 3px; white-space: nowrap; }
  .contact-list svg { width: 12px; height: 12px; flex: none; }
  .contact-list .email { font-size: 11px; }
</style>
</head>
<body>

  <section class="card card-back" aria-label="Card back with note lines">
    <div class="top-band"></div>
    <div class="band-rule"></div>
    <ul class="note-fields">
      <li class="note-field">
        <span class="note-label">DATE</span>
        <svg class="note-line" viewBox="0 0 280 12"><line x1="0" y1="10" x2="272" y2="10" stroke="var(--rule)" stroke-width="1.2"/><circle cx="275" cy="10" r="2.5" fill="var(--rule)"/></svg>
      </li>
      <li class="note-field">
        <span class="note-label">OCCUPATION</span>
        <svg class="note-line" viewBox="0 0 280 12"><line x1="0" y1="10" x2="272" y2="10" stroke="var(--rule)" stroke-width="1.2"/><circle cx="275" cy="10" r="2.5" fill="var(--rule)"/></svg>
      </li>
      <li class="note-field">
        <span class="note-label">INTERESTS</span>
        <svg class="note-line" viewBox="0 0 280 12"><line x1="0" y1="10" x2="272" y2="10" stroke="var(--rule)" stroke-width="1.2"/><circle cx="275" cy="10" r="2.5" fill="var(--rule)"/></svg>
      </li>
    </ul>
  </section>

  <section class="card card-front" aria-label="Card front with contact details">
    <div class="brand">
      <div class="brand-name"><span>BRIVO HOLDINGS LLC</span><span class="brand-dot"></span></div>
      <p class="brand-tagline">Providing clean, safe, and affordable housing</p>
    </div>
    <div class="contact">
      <p class="contact-name">Mark Dunthorpe</p>
      <p class="contact-address">12345, Address Goes Here<br>Country Name, 123456</p>
      <ul class="contact-list">
        <li>
          <svg viewBox="0 0 24 24"><path fill="var(--ink)" d="M6.6 10.8a15.1 15.1 0 0 0 6.6 6.6l2.2-2.2a1 1 0 0 1 1-.25 11.4 11.4 0 0 0 3.6.57 1 1 0 0 1 1 1V20a1 1 0 0 1-1 1A17 17 0 0 1 3 4a1 1 0 0 1 1-1h3.5a1 1 0 0 1 1 1c0 1.25.2 2.45.57 3.6a1 1 0 0 1-.25 1z"/></svg>
          <span>480-555-3174</span>
        </li>
        <li>
          <svg viewBox="0 0 24 24"><rect x="2" y="5" width="20" height="14" fill="var(--ink)"/><path d="M2 5l10 8 10-8" fill="none" stroke="var(--teal)" stroke-width="1.8"/></svg>
          <span class="email">markdunthorpe@brivoholdings.example</span>
        </li>
        <li>
          <svg viewBox="0 0 24 24"><circle cx="12" cy="12" r="10" fill="var(--ink)"/><path d="M2 12h20M12 2c3 3 3 17 0 20M12 2c-3 3-3 17 0 20" fill="none" stroke="var(--teal)" stroke-width="1.3"/></svg>
          <span>www.brivoholdings.example</span>
        </li>
      </ul>
    </div>
  </section>

</body>
</html>
```